Business to Business Website Homepage Design

Hi, My Web Developer is giving me designs that aren't quite taking my fancy as far as visual impact. I'd love to see designs come out which are simple, fresh and powerful.
I just want a PDF document that I can give to my web developer to follow, so this project is NOT to make a website, its to design the homepage.
I would like it to scroll down through different areas of my website on the homepage. Our colours are Blood Orange, White, Grey & Black.
I like these websites:
Simplicity
https://www.quenzaro.com/au/webapps/mpp/home
Our Team Section
http://bremlitch.com.au/
We'd like our logo on top left. Nav bar top right. Have an image which we can place a headline subject on + video icon which will pop out with a video and opt in for name and email with a heading so people know what they're opting in for.
The next section should have a lot of white space, this "What we do" which is 1) Grow in size so your business can get bigger 2) increase in value, so you maximise what your business is worth 3) Free up your time, so you can live the lifestyle you've always wanted. Our brief was we want image/text combo with a lot of white space,
Then we have our services
After Services, would like to have a "Why Work With Us" section
Then a testimonials section
Then "Our Team"
Then contact us.
Thats pretty much it, we'd just love some different ideas, these guys are almost there, but just need more impact.
Updates
Target Market(s)
Business Owners between $1m to $3m turnover
Industry/Entity Type
Business
Number of Pages Required
1 page
Look and feel
Each slider illustrates characteristics of the customer's brand and the style your logo design should communicate.

```html
<!DOCTYPE html>
<html lang="en">
<head>
<meta charset="utf-8">
<title>Trelwyn Group — Home</title>
<link href="https://fonts.googleapis.com/css2?family=Open+Sans:wght@400;600;700;800&display=swap" rel="stylesheet">
<style>
:root{
  --orange:#e8492c;
  --orange-deep:#d63a1f;
  --black:#111111;
  --charcoal:#1d1d1d;
  --grey:#6b6b6b;
  --grey-light:#e6e6e6;
  --white:#ffffff;
}
*{box-sizing:border-box;margin:0;padding:0}
html,body{width:1200px;height:3972px;overflow:hidden}
body{font-family:"Open Sans",Arial,sans-serif;color:var(--black);background:var(--white);position:relative}
.section{position:absolute;left:0;width:1200px}
.title{font-weight:800;font-size:34px;text-align:center;letter-spacing:.5px;text-transform:uppercase}
.title::after{content:"";display:block;width:60px;height:3px;background:var(--orange);margin:10px auto 0}
.btn{display:inline-block;background:var(--orange);color:var(--white);font-weight:700;text-transform:uppercase;text-align:center;white-space:nowrap}

/* header + hero */
.hero{top:0;height:688px;background:linear-gradient(100deg,#c9ccd0 0%,#aeb3b9 40%,#8d8f93 70%,#5f5a57 100%)}
.hero-photo{position:absolute;inset:0}
.site-header{position:absolute;top:0;left:0;width:1200px;height:56px;background:rgba(255,255,255,.92);display:flex;align-items:center;justify-content:space-between;padding:0 150px}
.brand{font-weight:700;font-size:20px;color:var(--charcoal)}
.nav{display:flex;gap:30px;align-items:center;font-size:13px;font-weight:600;text-transform:uppercase;color:var(--charcoal)}
.nav .btn{padding:7px 16px;font-size:12px}
.tags{position:absolute;top:160px;left:240px;width:720px;height:90px}
.tag{position:absolute;background:rgba(20,20,20,.82);color:var(--white);font-weight:700;font-size:28px;padding:8px 18px;text-transform:uppercase;white-space:nowrap}
.tag.one{left:0;top:0}.tag.two{left:230px;top:40px}.tag.three{left:470px;top:0}
.play{position:absolute;top:340px;left:560px;width:80px;height:80px}
.offer{position:absolute;top:486px;width:1200px;text-align:center;color:var(--white);font-size:30px;font-weight:600}
.optin{position:absolute;top:560px;left:280px;display:flex;gap:20px}
.field{width:230px;height:48px;background:var(--white);font-size:15px;color:var(--grey);padding:14px}
.optin .btn{width:150px;height:48px;line-height:48px;font-size:16px}

/* what we do */
.what{top:688px;height:400px}
.what .title{margin-top:30px}
.intro{width:800px;margin:22px auto 0;font-size:13px;color:var(--grey);text-align:center;line-height:1.5}
.pillars{position:absolute;top:182px;left:140px;display:flex;gap:20px}
.pillar{width:292px;height:160px;background:var(--charcoal);color:var(--white);text-align:center;position:relative;padding-top:40px}
.pillar.active{background:var(--orange)}
.pillar-num{position:absolute;top:-22px;left:124px;width:44px;height:44px;border-radius:50%;background:var(--black);border:3px solid var(--white);font-weight:800;font-size:22px;line-height:38px}
.pillar h3{font-size:20px;font-weight:600;text-transform:uppercase}
.pillar p{font-size:13px;margin:14px 30px 0;line-height:1.4;opacity:.9}

/* mission */
.mission{top:1088px;height:312px;background:linear-gradient(90deg,#2a2c30,#45484d 50%,#2a2c30);color:var(--white);text-align:center}
.mission .title{margin-top:100px;color:var(--white)}
.mission p{font-size:26px;width:760px;margin:28px auto 0;line-height:1.35}

/* services */
.services{top:1400px;height:560px;background:linear-gradient(180deg,#f06a3a,var(--orange-deep));color:var(--white)}
.services .title{margin-top:150px}
.services .title::after{background:var(--white)}
.service-list{position:absolute;top:290px;left:190px;display:flex;gap:30px}
.service{width:200px;text-align:center}
.service-icon{width:70px;height:70px;border-radius:50%;border:3px solid var(--white);margin:0 auto}
.service h4{font-size:15px;font-weight:800;margin-top:14px;text-transform:uppercase;white-space:nowrap}
.service p{font-size:12px;margin:8px 10px 0;line-height:1.4}
.service .more{display:inline-block;margin-top:14px;background:var(--black);font-size:11px;font-weight:700;padding:7px 16px}
.arrow{position:absolute;top:312px;width:36px;height:36px;border-radius:50%;background:var(--charcoal)}
.arrow.left{left:118px}.arrow.right{right:118px}

/* why */
.why{top:1960px;height:500px}
.why .title{margin-top:52px}
.why-visual{position:absolute;top:140px;left:90px;width:270px;height:270px;border-radius:8px;background:linear-gradient(150deg,#f06a3a,#b83a22)}
.reasons{position:absolute;top:140px;left:400px;list-style:none}
.reasons li{display:flex;align-items:center;gap:14px;height:56px;font-size:14px;font-weight:800;text-transform:uppercase}
.reasons span{width:34px;height:34px;border-radius:50%;background:var(--orange);color:var(--white);text-align:center;line-height:34px;font-size:16px}
.brace{position:absolute;top:130px;left:650px}
.why-text{position:absolute;top:140px;left:760px;width:350px;font-size:13px;color:var(--grey);line-height:1.6}
.why-text p+p{margin-top:16px}

/* team */
.team{top:2460px;height:1020px}
.team .title{margin-top:10px}
.team-intro{width:700px;margin:12px auto 0;text-align:center;font-size:12px;color:var(--grey);line-height:1.5}
.team-grid{position:absolute;top:120px;left:0;display:grid;grid-template-columns:repeat(4,300px);grid-auto-rows:300px}
.member{position:relative}
.member.a{background:linear-gradient(160deg,#b8b8b8,#3c3c3c)}
.member.b{background:linear-gradient(160deg,#d86b44,#2b2b2b)}
.member.c{background:linear-gradient(160deg,#eee,#9a8a78)}
.member.d{background:linear-gradient(160deg,#d7d9dc,#4c5058)}
.member.e{background:linear-gradient(160deg,#e8a26f,#7d5f4b)}
.member.feature{background:var(--orange-deep);color:var(--white);text-align:center}
.feature-info{position:absolute;bottom:36px;width:100%}
.feature-info h5{font-size:18px;font-weight:700}
.feature-info small{font-size:13px;display:block;margin-top:2px}
.follow{display:inline-flex;align-items:center;gap:8px;margin-top:10px;font-size:16px}
.follow i{width:18px;height:18px;border-radius:50%;background:var(--white)}

/* cta */
.cta{top:3480px;height:112px;background:var(--black);color:var(--white)}
.cta-text{position:absolute;left:150px;top:30px}
.cta-text strong{font-size:20px;font-weight:700;display:block}
.cta-text span{font-size:15px;opacity:.85}
.cta .btn{position:absolute;right:150px;top:32px;width:200px;height:48px;line-height:48px;font-size:16px}

/* testimonials + contact */
.lower{top:3592px;height:348px;background:linear-gradient(90deg,var(--white) 0 55%,#2b2b2b 55%)}
.testimonial{position:absolute;left:130px;top:20px;width:480px}
.sub-title{font-size:20px;font-weight:800;text-transform:uppercase}
.quote{display:flex;gap:20px;margin-top:34px}
.quote-photo{width:140px;height:180px;background:linear-gradient(160deg,#d2d2d2,#3d3d3d);flex:none}
.quote h6{font-size:13px;font-weight:800;text-transform:uppercase}
.quote small{font-size:11px;color:var(--grey)}
.quote p{font-size:12px;color:var(--grey);margin-top:10px;line-height:1.5}
.dots{display:flex;gap:6px;margin:20px 0 0 230px}
.dots i{width:8px;height:8px;border-radius:50%;background:#999}.dots i:first-child{background:var(--black)}
.contact{position:absolute;left:720px;top:20px;width:350px;color:var(--white)}
.contact .sub-title{text-align:center}
.contact .row{height:32px;background:var(--white);color:var(--grey);font-size:12px;padding:8px 10px;margin-top:10px}
.contact .msg{height:70px}
.contact .send{display:flex;align-items:center;gap:14px;margin-top:10px;font-size:11px}
.contact .send .btn{padding:8px 14px;font-size:11px}

/* footer */
.footer{top:3940px;height:32px;background:var(--charcoal);color:#aaa;font-size:11px;display:flex;align-items:center;justify-content:space-between;padding:0 150px}
.social{display:flex;gap:10px}.social i{width:20px;height:20px;border-radius:50%;border:1px solid #888}
</style>
</head>
<body>

<section class="section hero">
  <div class="hero-photo" role="img" aria-label="Businessman in a suit smiling in a bright office with colleagues behind"></div>
  <header class="site-header">
    <div class="brand">Trelwyn Group</div>
    <nav class="nav"><span>Home</span><span>Services</span><span>Events</span><span>Jobs</span><span>Contact</span><span class="btn">Subscribe</span></nav>
  </header>
  <div class="tags">
    <span class="tag one">Your Business</span>
    <span class="tag two">Your Success</span>
    <span class="tag three">Your Life Style</span>
  </div>
  <svg class="play" viewBox="0 0 80 80"><circle cx="40" cy="40" r="40" fill="#111"/><path d="M32 24 L58 40 L32 56Z" fill="#fff"/></svg>
  <h2 class="offer">Get a Complementary 60 Minute Consultation</h2>
  <form class="optin"><div class="field">Name</div><div class="field">Email</div><div class="btn">Sign Up</div></form>
</section>

<section class="section what">
  <h2 class="title">What we do is help businesses</h2>
  <p class="intro">We partner with owners to build stronger, more valuable companies that run smoothly without constant oversight, giving you the freedom to step back and enjoy what you built.</p>
  <div class="pillars">
    <div class="pillar active"><span class="pillar-num">1</span><h3>Grow your business</h3><p>Boost turnover with clear plans and proven growth strategies.</p></div>
    <div class="pillar"><span class="pillar-num">2</span><h3>Increase in value</h3><p>Raise what your company is worth with sound systems.</p></div>
    <div class="pillar"><span class="pillar-num">3</span><h3>Free up your time</h3><p>Step back from daily work and enjoy the life you want.</p></div>
  </div>
</section>

<section class="section mission" role="img" aria-label="Business team in a meeting, darkened background">
  <h2 class="title">Our Mission</h2>
  <p>We exist to help people create better livelihoods so they can follow their dreams and live. life to its fullest</p>
</section>

<section class="section services">
  <h2 class="title">Our Services</h2>
  <svg class="arrow left" viewBox="0 0 36 36"><circle cx="18" cy="18" r="18" fill="#1d1d1d"/><path d="M21 11 L14 18 L21 25" stroke="#fff" stroke-width="3" fill="none"/></svg>
  <div class="service-list">
    <div class="service"><div class="service-icon"></div><h4>People</h4><p>Build a capable team that drives results every day.</p><span class="more">Read More</span></div>
    <div class="service"><div class="service-icon"></div><h4>Business Systems</h4><p>Put smart processes in place so work runs smoothly.</p><span class="more">Read More</span></div>
    <div class="service"><div class="service-icon"></div><h4>Funding</h4><p>Find the right capital to fund your next stage.</p><span class="more">Read More</span></div>
    <div class="service"><div class="service-icon"></div><h4>New Earning Streams</h4><p>Open fresh income sources to lift your turnover.</p><span class="more">Read More</span></div>
  </div>
  <svg class="arrow right" viewBox="0 0 36 36"><circle cx="18" cy="18" r="18" fill="#1d1d1d"/><path d="M15 11 L22 18 L15 25" stroke="#fff" stroke-width="3" fill="none"/></svg>
</section>

<section class="section why">
  <h2 class="title">Why work with us</h2>
  <div class="why-visual" role="img" aria-label="Feature image for the why work with us section"></div>
  <ol class="reasons">
    <li><span>1</span>Innovation</li>
    <li><span>2</span>Strategies</li>
    <li><span>3</span>Growth</li>
    <li><span>4</span>Expertise</li>
    <li><span>5</span>Results</li>
  </ol>
  <svg class="brace" width="60" height="300" viewBox="0 0 60 300"><path d="M10 5 Q35 5 35 40 L35 120 Q35 150 55 150 Q35 150 35 180 L35 260 Q35 295 10 295" stroke="#ccc" stroke-width="3" fill="none"/></svg>
  <div class="why-text">
    <p>We bring fresh thinking and practical plans drawn from years running real companies. Every strategy is shaped around your goals, your market and the stage your business has reached today.</p>
    <p>Our advisers stay with you from first review to final result, measuring progress each month so growth is steady, value keeps rising and you win back time.</p>
  </div>
</section>

<section class="section team">
  <h2 class="title">Our Team</h2>
  <p class="team-intro">Experienced advisers who have built, grown and sold businesses of their own, now helping owners do the same.</p>
  <div class="team-grid">
    <div class="member b" role="img" aria-label="Portrait of a male adviser"></div>
    <div class="member d" role="img" aria-label="Portrait of a male adviser"></div>
    <div class="member c" role="img" aria-label="Portrait of a female adviser"></div>
    <div class="member a" role="img" aria-label="Portrait of a male adviser"></div>
    <div class="member e" role="img" aria-label="Portrait of a female adviser"></div>
    <div class="member a" role="img" aria-label="Portrait of a male adviser"></div>
    <div class="member feature">
      <div class="feature-info"><h5>Nolan Brecker</h5><small>Senior Graphic Designer</small><span class="follow"><i></i>Follow</span></div>
    </div>
    <div class="member c" role="img" aria-label="Portrait of a female adviser"></div>
    <div class="member b" role="img" aria-label="Portrait of a male adviser"></div>
    <div class="member d" role="img" aria-label="Portrait of a male adviser"></div>
    <div class="member a" role="img" aria-label="Portrait of a male adviser"></div>
    <div class="member c" role="img" aria-label="Portrait of a male adviser with glasses"></div>
  </div>
</section>

<section class="section cta">
  <div class="cta-text"><strong>Lorem ipsum dolor sit amet consectetuer adipiscing elit magna</strong><span>Duis autem vel eum iriure dolor in hendrerit dolore eu feugiat nulla</span></div>
  <span class="btn">Call to Action</span>
</section>

<section class="section lower">
  <div class="testimonial">
    <h3 class="sub-title">What our customer say</h3>
    <div class="quote">
      <div class="quote-photo" role="img" aria-label="Portrait of a client in a suit"></div>
      <div><h6>Tessa Marlow</h6><small>Managing Director</small><p>Working with the team changed how we run our company. Turnover is up and I finally have time for my family.</p></div>
    </div>
    <div class="dots"><i></i><i></i><i></i><i></i></div>
  </div>
  <div class="contact">
    <h3 class="sub-title">Contact Us</h3>
    <div class="row">Name</div><div class="row">Email</div><div class="row">Phone</div><div class="row msg">Message</div>
    <div class="send"><span class="btn">Send Message</span><span>We reply within one working day</span></div>
  </div>
</section>

<footer class="section footer">
  <span>© 2015 Trelwyn Group All Rights Reserved</span>
  <div class="social"><i></i><i></i><i></i><i></i><i></i></div>
</footer>

</body>
</html>
```